Website design for Maple Nook Kidcare

I need a website designed for my daycare business, Maple Nook Kidcare, now that I have a new logo. My former website was ok but simple and I did not have a logo yet. It also was created by me using a template and was entirely pink. I loved the bright, happy feel of it but worried it might not appeal as much to potential clients who have sons. Therefore, I need a site which will appeal to both genders while still keeping the cheerful color scheme of my new logo, which has pinks, blue, green and cream.

Reason: Hello! I am still trying to download my new logo and am sorry it is taking me so long. Hopefully I will it posted by the end of today (US Eastern Standard Time). Thank you all very much for your patience!

Hello! I have finally managed to upload my new logo for you to use in designing my website. I'm sorry it took so long and greatly appreciate your time and creative efforts! I look forward to seeing what is submitted based on my logo design and its style/colors.

Many thanks!

Reason: As I've been traveling and posted my logo file late, I am extending my deadline. I am now back and can focus on providing more and better feedback. I appreciate your patience and submissions very much!

Reason: I need more time to provide feedback and make decisions.

Industry/Entity Type

Daycare

Colors
0192cd
33a6d7
86cae7
cadf82
fbf289
add136
e34197

```html
<!DOCTYPE html>
<html lang="en">
<head>
<meta charset="utf-8">
<title>Maple Nook Kidcare</title>
<link href="https://fonts.googleapis.com/css2?family=Signika:wght@400;600&family=Source+Sans+3:wght@400;600&display=swap" rel="stylesheet">
<style>
:root{
  --green:#8cc63f;
  --green-bar:#b5d55a;
  --green-title:#7ab531;
  --pink:#e34197;
  --pink-soft:#f08bc2;
  --teal:#5fc3cc;
  --blue-link:#33a6d7;
  --brown:#7a5a3c;
  --text:#6a7585;
  --footer-bg:#f6f5ef;
  --map-tone:#e4e4df;
  --white:#ffffff;
}
*{box-sizing:border-box;margin:0;padding:0}
html,body{width:1024px;height:1200px;overflow:hidden;background:var(--white)}
body{position:relative;font-family:"Source Sans 3",sans-serif;color:var(--text)}

/* header */
.site-header{position:absolute;left:0;top:0;width:1024px;height:117px;background:var(--green);z-index:3}
.brand-box{position:absolute;left:136px;top:0;width:154px;height:132px;background:var(--white);border-radius:0 0 4px 4px;box-shadow:0 1px 4px rgba(0,0,0,.15);display:flex;align-items:center;justify-content:center;z-index:4}
.brand-name{font-family:"Signika",sans-serif;font-weight:600;color:var(--pink);font-size:22px;line-height:1.05;text-align:center}
.brand-dot{width:14px;height:14px;border-radius:50%;background:var(--green);margin:0 auto 8px}
.topbar{position:absolute;top:0;left:441px;height:41px;display:flex;align-items:center;font-size:11px;color:var(--white)}
.topbar .item{display:flex;align-items:center;gap:7px;padding:0 11px 0 14px;height:41px;border-left:1px solid rgba(255,255,255,.3)}
.topbar svg{width:16px;height:16px;stroke:rgba(255,255,255,.55);fill:none;stroke-width:1.6}
.main-nav{position:absolute;top:58px;left:308px;display:flex}
.main-nav a{display:flex;flex-direction:column;align-items:center;gap:8px;text-decoration:none;color:#f1f7e6;font-size:12px;padding:0 15px;position:relative}
.main-nav a svg{width:20px;height:20px;fill:rgba(255,255,255,.35)}
.main-nav a.active{color:var(--white)}
.main-nav a.active svg{fill:var(--white)}
.main-nav a.active::after{content:"";position:absolute;bottom:-24px;left:50%;margin-left:-9px;border:9px solid transparent;border-bottom-color:var(--white)}

/* hero */
.hero{position:absolute;left:0;top:117px;width:1024px;height:466px;background:
  linear-gradient(180deg,rgba(255,255,255,0) 55%,rgba(255,255,255,.55) 100%),
  linear-gradient(100deg,#e9dccc 0%,#c7a07b 30%,#d9b59a 50%,#e9d9c8 70%,#c4955f 90%,#eadccd 100%)}
.hero-title{position:absolute;left:0;top:380px;width:1024px;text-align:center;font-family:"Signika",sans-serif;font-weight:600;font-size:35px;line-height:46px;color:var(--white);text-shadow:0 2px 6px rgba(0,0,0,.35);z-index:2}

/* features card */
.card{position:absolute;left:129px;top:490px;width:767px;height:510px;background:var(--white);border-radius:10px 10px 0 0;box-shadow:0 0 4px rgba(0,0,0,.08)}
.feature{position:absolute;top:22px;width:250px;text-align:center}
.feature .photo{width:146px;height:146px;border-radius:50%;margin:0 auto}
.feature h2{font-family:"Signika",sans-serif;font-weight:600;font-size:18px;margin-top:18px;letter-spacing:.3px}
.feature p{font-size:11.5px;line-height:16px;margin:7px auto 0;width:228px}
.learning h2{color:var(--green-title)}
.creativity h2{color:var(--pink)}
.sharing h2{color:var(--teal)}

.about-photo{position:absolute;left:25px;top:327px;width:111px;height:152px;background:linear-gradient(160deg,#bfe3ef,#f5d9b8 55%,#e3a869)}
.about{position:absolute;left:152px;top:329px;width:325px}
.section-title{font-family:"Signika",sans-serif;font-weight:600;font-size:14px;color:var(--brown)}
.about p{font-size:10.5px;line-height:14.5px;margin-top:15px}
.about p+p{margin-top:14px}
.link{display:inline-block;margin-top:16px;font-size:8px;color:var(--blue-link);text-decoration:underline;letter-spacing:.3px}
.news{position:absolute;left:521px;top:329px;width:240px}
.news-item{display:flex;gap:17px;margin-top:15px}
.news-item+.news-item{margin-top:26px}
.date{flex:none;width:47px;height:47px;background:var(--pink-soft);color:var(--white);text-align:center;font-family:"Signika",sans-serif}
.date b{display:block;font-weight:400;font-size:17px;line-height:22px;padding-top:5px}
.date small{font-size:7px}
.news-item p{font-size:10.5px;line-height:16px;width:168px}
.news-item .more{font-size:7px;color:var(--blue-link);font-weight:600;white-space:nowrap}

/* footer */
.site-footer{position:absolute;left:0;top:1000px;width:1024px;height:165px;background:var(--footer-bg);border-top:1px solid #e8e6dc}
.footer-brand{position:absolute;left:136px;top:36px;width:130px;text-align:center}
.footer-col{position:absolute;top:36px}
.footer-col h3{font-family:"Signika",sans-serif;font-weight:600;font-size:10.5px;color:var(--brown);margin-bottom:11px}
.footer-col ul{list-style:none}
.footer-col li{font-size:10px;color:#7a8593;line-height:19.2px;padding-left:10px;position:relative;letter-spacing:.3px;white-space:nowrap}
.footer-col li::before{content:"";position:absolute;left:0;top:7px;border:3px solid transparent;border-left-color:#c9c6b8}
.nav-col li:first-child{color:var(--green-title)}
.contact-list li{padding-left:18px;line-height:24px}
.contact-list li::before{display:none}
.contact-list svg{position:absolute;left:0;top:7px;width:10px;height:10px;fill:#c5c9cc}
.map{position:absolute;left:714px;top:54px;width:174px;height:81px;border-radius:3px;background:var(--map-tone)}
.bottom-bar{position:absolute;left:0;top:1165px;width:1024px;height:35px;background:var(--green-bar);color:var(--white);font-size:10px}
.bottom-bar .copy{position:absolute;left:135px;top:11px}
.bottom-bar .legal{position:absolute;right:136px;top:11px}
</style>
</head>
<body>

<header class="site-header">
  <div class="topbar">
    <div class="item">
      <svg viewBox="0 0 16 16"><circle cx="8" cy="9" r="5.5"/><path d="M8 6v3l2 1"/></svg>
      (Mon - Fri) 8:00AM to 6:00PM
    </div>
    <div class="item">
      <svg viewBox="0 0 16 16"><rect x="2" y="4" width="12" height="8"/><path d="M2 4l6 5 6-5"/></svg>
      hello@maplenookmail.com
    </div>
    <div class="item">
      <svg viewBox="0 0 16 16"><path d="M4 2l3 3-2 2c1 2 2 3 4 4l2-2 3 3-2 2C7 14 2 9 2 4z"/></svg>
      +(555) 014-2290
    </div>
  </div>
  <nav class="main-nav">
    <a class="active" href="#"><svg viewBox="0 0 20 20"><path d="M10 2l8 7h-2v9h-4v-5H8v5H4V9H2z"/></svg>Home</a>
    <a href="#"><svg viewBox="0 0 20 20"><circle cx="10" cy="7" r="4"/><path d="M3 18c0-4 3-6 7-6s7 2 7 6z"/></svg>About</a>
    <a href="#"><svg viewBox="0 0 20 20"><path d="M2 4h7v13H2zM11 4h7v13h-7z"/></svg>Services</a>
    <a href="#"><svg viewBox="0 0 20 20"><path d="M10 1a9 9 0 1 0 0 18 9 9 0 0 0 0-18zm-1 4h2v5l3 2-1 1.5-4-2.5z"/></svg>Hours &amp; Fees</a>
    <a href="#"><svg viewBox="0 0 20 20"><path d="M4 3h12v16H4zM7 1h6v3H7z"/></svg>Policies</a>
    <a href="#"><svg viewBox="0 0 20 20"><path d="M2 6h4l2-2h4l2 2h4v11H2zM10 8a3 3 0 1 0 0 6 3 3 0 0 0 0-6z"/></svg>Photos</a>
    <a href="#"><svg viewBox="0 0 20 20"><path d="M2 4h16v9H9l-4 4v-4H2z"/></svg>Testimonials</a>
    <a href="#"><svg viewBox="0 0 20 20"><path d="M1 4h18v12H1zM1 4l9 7 9-7"/></svg>Contact</a>
  </nav>
</header>

<div class="brand-box">
  <div>
    <div class="brand-dot"></div>
    <div class="brand-name">Maple Nook<br>Kidcare</div>
  </div>
</div>

<section class="hero" role="img" aria-label="Photo of three laughing toddlers jumping in a playroom with toys and a wooden rocking horse"></section>
<h1 class="hero-title">Maple Nook Kidcare - a playspace where children<br>can play, create, and imagine!</h1>

<main class="card">
  <div class="feature learning" style="left:0">
    <div class="photo" role="img" aria-label="Photo of children playing together at a table" style="background:radial-gradient(circle at 50% 40%,#f0d2b0,#b8823e 70%,#8a5f2a)"></div>
    <h2>LEARNING</h2>
    <p>We develop age-appropriate activities that introduce and strengthen academic and to hone their social skills.</p>
  </div>
  <div class="feature creativity" style="left:258px">
    <div class="photo" role="img" aria-label="Photo of a smiling child with a paint-covered hand" style="background:radial-gradient(circle at 45% 45%,#f3d3c2,#c89a8a 55%,#4a5a3a)"></div>
    <h2>CREATIVITY</h2>
    <p>We offer children a wide range of creative opportunities including art projects, toddler yoga lessons, and a large selection of books and games.</p>
  </div>
  <div class="feature sharing" style="left:516px">
    <div class="photo" role="img" aria-label="Photo of a child and a woman sharing a pretend tea party" style="background:radial-gradient(circle at 50% 45%,#f2ddc6,#c79a72 60%,#7a5a40)"></div>
    <h2>SHARING</h2>
    <p>We strive to include enrichment activities that extend your child's understanding of the world and their role in it.</p>
  </div>

  <div class="about-photo" role="img" aria-label="Photo of children drawing with a teacher"></div>
  <div class="about">
    <h2 class="section-title">About Maple Nook Kidcare</h2>
    <p>We are a few blocks from the 4 line subway and the 12th Street bus route, and we offer flexible hourly childcare, making it as easy as possible for busy parents on the go to arrange their children's care.</p>
    <p>We invite you to learn more about us and hope you will visit us soon</p>
    <a class="link" href="#">READ MORE</a>
  </div>

  <div class="news">
    <h2 class="section-title">Latest News</h2>
    <div class="news-item">
      <div class="date"><b>05</b><small>May 2014</small></div>
      <p>We are thrilled to have found a new cheerful space with a private backyard... <span class="more">&#9656;READ MORE</span></p>
    </div>
    <div class="news-item">
      <div class="date"><b>05</b><small>May 2014</small></div>
      <p>We are thrilled to have found a new cheerful space with a private backyard... <span class="more">&#9656;READ MORE</span></p>
    </div>
  </div>
</main>

<footer class="site-footer">
  <div class="footer-brand">
    <div class="brand-dot"></div>
    <div class="brand-name">Maple Nook<br>Kidcare</div>
  </div>
  <div class="footer-col nav-col" style="left:312px">
    <h3>Navigation</h3>
    <ul><li>Home</li><li>About</li><li>Services</li><li>Contact</li></ul>
  </div>
  <div class="footer-col" style="left:438px">
    <h3>Links</h3>
    <ul><li>Hours &amp; Fees</li><li>Policies</li><li>Testimonials</li><li>Photos</li></ul>
  </div>
  <div class="footer-col" style="left:566px">
    <h3>Contact Us</h3>
    <ul class="contact-list">
      <li><svg viewBox="0 0 10 10"><path d="M2 0l2 2-1 1.5c.6 1.2 1.3 1.9 2.5 2.5L7 5l2 2-1.5 2C3 8.5 1 6 1 1.5z"/></svg>+1 (555) 014-7731</li>
      <li><svg viewBox="0 0 10 10"><path d="M0 2h10v6H0z"/></svg>office@maplenookmail.com</li>
      <li style="line-height:19px;padding-top:3px"><svg viewBox="0 0 10 10"><path d="M5 0a3.5 3.5 0 0 0-3.5 3.5C1.5 6 5 10 5 10s3.5-4 3.5-6.5A3.5 3.5 0 0 0 5 0z"/></svg>Address, Your Country<br>Your Zip Code</li>
    </ul>
  </div>
  <div class="footer-col" style="left:715px">
    <h3>Visit Us</h3>
  </div>
  <div class="map" role="img" aria-label="Map showing the daycare location"></div>
</footer>

<div class="bottom-bar">
  <span class="copy">Copyright 2014 &copy; Maple Nook Kidcare - All Rights Reserved</span>
  <span class="legal">Site Map &nbsp;&nbsp;&bull;&nbsp;&nbsp; Privacy Policy</span>
</div>

</body>
</html>
```